Etiketten-Design für Eierschachtel
Zielgruppe
Wir haben einen Hofladen, indem wir unsere hofeigenen Produkte direkt an den Verbraucher verkaufen.
Aufgabenstellung
Wir suchen ein Etikett für unsere Eierschachtel, die wir für den Verkauf unserer Eier im eigenen Hofladen benötigen.
Das Etikett soll hell und freundlich, aber keinesfalls überladen oder zu verspielt sein. Es soll die Natürlichkeit und Regionalität widerspiegeln. Wir halten unsere Hühner in mobiler Freilandhaltung mit ausreichend Auslauf auf unseren Wiesen.
Das beigefügte Logo (einmal farbig, einmal schwarz/weiß - je nach Vorschlag was besser passt) soll integriert werden.
Das Etikett soll folgende Punkte enthalten:
Rückseite:
- 'Verbraucherhinweis: Nach dem Kauf bei Kühlschranktemperatur aufbewahren. Nach Ablauf des
Mindesthaltbarkeitsdatums durcherhitzen.'
- Familie Haslbeck
Lindenweg 7
84273 Moosreith
Vorderseite (zum Öffnen der Eierschachtel) bzw. Deckel oben:
- '10 frische Eier aus mobiler Freilandhaltung' (gerne auch eigene Vorschläge von Ihnen)
- passender Slogan, der auf Regionalität bzw. Einkaufen direkt beim Erzeuger basiert
Format: ca. 21,4cm breit und ca. 14,2cm lang

```html
<!DOCTYPE html>
<html lang="de">
<head>
<meta charset="utf-8">
<title>Eierschachtel-Etikett – Haslbeck Hof</title>
<link href="https://fonts.googleapis.com/css2?family=Source+Sans+3:wght@400;600;700&display=swap" rel="stylesheet">
<style>
  :root {
    --green: #1b8212;
    --brown: #7a2d02;
    --white: #ffffff;
    --page: #ffffff;
    --egg: #f3eee6;
    --logo-green: #2b8a2a;
  }
  * { margin: 0; padding: 0; box-sizing: border-box; }
  html, body { width: 922px; height: 1200px; overflow: hidden; background: var(--page); }
  body { font-family: "Source Sans 3", Arial, sans-serif; position: relative; }

  .label {
    position: absolute; left: 31px; top: 372px;
    width: 860px; height: 456px;
  }
  .band-back {
    height: 82px; background: var(--green); color: var(--white);
    position: relative;
  }
  .notice { position: absolute; left: 49px; top: 22px; }
  .notice-title, .sender-name {
    font-weight: 600; font-size: 12px; text-decoration: underline;
    margin-bottom: 3px;
  }
  .notice-text, .sender-address { font-size: 8.5px; line-height: 1.35; font-weight: 600; }
  .sender { position: absolute; left: 697px; top: 22px; }

  .hero {
    height: 292px; position: relative; overflow: hidden;
  }
  .hero-photo {
    position: absolute; inset: 0;
    background:
      radial-gradient(ellipse 130px 170px at 570px 170px, #b5642a 0%, #a0531f 55%, rgba(160,83,31,0) 100%),
      radial-gradient(ellipse 260px 200px at 760px 120px, #6fae3c 0%, rgba(111,174,60,0) 100%),
      linear-gradient(90deg, #e4e6e3 0%, #d2d6cf 25%, #8f9e7e 48%, #5f8f3a 65%, #7bb84a 85%, #9fcf6c 100%);
  }

  .farm-name {
    position: absolute; left: 64px; top: 64px; width: 180px;
    text-align: center; color: var(--logo-green);
  }
  .farm-mark { display: block; margin: 0 auto 14px; }
  .farm-text { font-size: 21px; font-weight: 600; letter-spacing: 0.5px; }

  .headline {
    position: absolute; left: 240px; top: 98px; width: 305px; height: 62px;
    background: var(--brown); color: var(--white); padding: 5px 0 0 15px;
  }
  .headline-main { font-size: 28px; font-weight: 700; line-height: 1; letter-spacing: 0.2px; }
  .headline-sub { font-size: 14px; font-weight: 400; line-height: 1.1; }

  .count-badge {
    position: absolute; left: 670px; top: 204px; width: 78px; height: 100px;
    background: var(--egg); border-radius: 50% 50% 50% 50% / 58% 58% 42% 42%;
    text-align: center; color: var(--brown);
  }
  .count-number { font-size: 37px; font-weight: 700; line-height: 1; margin-top: 20px; }
  .count-text { font-size: 7.5px; font-weight: 700; }

  .band-slogan {
    height: 82px; background: var(--brown); color: var(--white);
    display: flex; align-items: center; justify-content: center;
    font-size: 22px; font-weight: 400;
  }
</style>
</head>
<body>
  <section class="label">
    <div class="band-back">
      <div class="notice">
        <p class="notice-title">Verbraucherhinweis:</p>
        <p class="notice-text">Nach dem Kauf bei Kühlschranktemperatur aufbewahren.<br>Nach Ablauf des Mindesthaltbarkeitsdatums durcherhitzen.</p>
      </div>
      <div class="sender">
        <p class="sender-name">Familie Haslbeck</p>
        <p class="sender-address">Lindenweg 7<br>84273 Moosreith</p>
      </div>
    </div>

    <div class="hero">
      <div class="hero-photo" role="img" aria-label="Foto: braunes Huhn im Grünen auf der Wiese, links unscharfer heller Hintergrund"></div>
      <div class="farm-name">
        <svg class="farm-mark" width="60" height="60" viewBox="0 0 60 60" aria-hidden="true">
          <circle cx="30" cy="30" r="28" fill="none" stroke="var(--logo-green)" stroke-width="1.5"/>
        </svg>
        <span class="farm-text">HASLBECK HOF</span>
      </div>
      <div class="headline">
        <p class="headline-main">FRISCHE EIER AUS</p>
        <p class="headline-sub">MOBILER FREILANDHALTUNG</p>
      </div>
      <div class="count-badge">
        <p class="count-number">10</p>
        <p class="count-text">FRISCHE EIER</p>
      </div>
    </div>

    <div class="band-slogan">Weil es aus der Region am besten ist</div>
  </section>
</body>
</html>
```